Happy Birthday Postcard for law firm for existing clients

Need a postcard that will go out to our current clients on their birthdays. Prefer to have our logo incorporated as part of the design so it reminds them about our business. The back needs to say "Happy Birthday from the team at Brantley Law Firm."

We are a law firm that services local clients. Needs to be mailed so the backside right half needs to be left blank except the return address (in NEEDS below) so it can be mailed with a mailing label.

Target Market(s)

existing customers, varying age range and demographic profile

Industry/Entity Type

Legal

Font styles to use
Sans Serif
Script

Colors

Designer to choose colors to be used in the design.

Requirements
Must have
• Our logo preferrably on the front (can be modified or added to so it fits a birthday message. And needs to be mailed so the back right side needs to be left open for address labels. The firms return address is
• Brantley Law Firm
• 7150 W Copperfield Ave
• Springfield, MO 65817
• Needs to have the text included in the project description on the back, or some close iteration of it if space is limited.
Nice to have
• Some illustration or graphic on the front with the logo that shows it is a birthday postcard

```html
<!DOCTYPE html>
<html lang="en">
<head>
<meta charset="utf-8">
<title>Brantley Law Firm – Birthday Postcard</title>
<link rel="stylesheet" href="https://fonts.googleapis.com/css2?family=Yellowtail&family=Comfortaa:wght@700&family=Cinzel:wght@400;700&family=Quicksand:wght@500&display=swap">
<style>
  :root {
    --backdrop: #0a6fbd;
    --card-white: #ffffff;
    --gold: #f7c531;
    --berry: #c2185b;
    --plum-dark: #2a1b45;
    --plum-mid: #6a2a6a;
    --rose: #a8244f;
    --maroon-dark: #3a1424;
    --maroon-mid: #6b2a3f;
    --ink-grey: #5e5e66;
    --rule-grey: #b9b9b9;
    --ribbon-dots: #333333;
  }
  * { margin: 0; padding: 0; box-sizing: border-box; }
  html, body { width: 800px; height: 1200px; overflow: hidden; }
  body { background: var(--backdrop); position: relative; }

  .postcard {
    position: absolute;
    left: 96px;
    width: 608px;
    height: 474px;
    overflow: hidden;
    box-shadow: 6px 6px 10px rgba(0,0,0,0.35);
    background: var(--card-white);
  }
  .postcard--front { top: 98px; }
  .postcard--back { top: 630px; }

  /* Front */
  .front-photo {
    position: absolute; inset: 0;
    background:
      radial-gradient(circle at 78% 80%, var(--rose) 0%, rgba(168,36,79,0.6) 30%, transparent 60%),
      radial-gradient(circle at 55% 15%, rgba(230,110,170,0.7) 0%, transparent 45%),
      linear-gradient(120deg, var(--plum-dark) 0%, var(--plum-mid) 55%, #8a2c5a 100%);
  }
  .greeting {
    position: absolute;
    left: 36px; top: 40px;
    font-family: "Yellowtail", cursive;
    color: var(--gold);
    font-size: 112px;
    line-height: 0.95;
    text-shadow: 3px 3px 0 #fff;
  }
  .greeting span { display: block; }
  .greeting .line-2 { margin-left: 8px; }
  .sender {
    position: absolute;
    left: 44px; top: 330px;
    font-family: "Comfortaa", sans-serif;
    font-weight: 700;
  }
  .sender__lead { color: #fff; font-size: 29px; line-height: 1.2; }
  .sender__firm {
    color: var(--berry);
    font-size: 31px;
    text-transform: uppercase;
    -webkit-text-stroke: 1px #fff;
    line-height: 1.2;
  }
  .ribbon { position: absolute; left: 400px; top: 0; width: 184px; height: 212px; }
  .ribbon__name {
    position: absolute;
    left: 400px; top: 78px; width: 184px;
    text-align: center;
    font-family: "Comfortaa", sans-serif;
    font-weight: 700;
    font-size: 19px;
    color: #8e8fb5;
  }
  .ribbon__mark {
    position: absolute;
    left: 478px; top: 44px;
    width: 28px; height: 28px;
    background: #b3b4d0;
  }

  /* Back */
  .back-photo {
    position: absolute; left: 0; top: 0; width: 306px; height: 100%;
    background:
      radial-gradient(circle at 75% 60%, rgba(190,60,100,0.55) 0%, transparent 50%),
      linear-gradient(160deg, var(--maroon-dark) 0%, var(--maroon-mid) 55%, #4a1e30 100%);
  }
  .contact {
    position: absolute; left: 14px; top: 54px;
    font-family: "Cinzel", serif; color: #fff;
  }
  .contact__tagline { font-size: 18px; line-height: 1.1; }
  .contact__value-word { font-size: 27px; font-weight: 700; line-height: 1.2; }
  .contact__label { font-size: 37px; line-height: 1; margin-top: 20px; }
  .contact__label--small { font-size: 24px; margin-top: 26px; }
  .contact__number { font-size: 24px; line-height: 1.25; }
  .contact__number--toll { margin-top: 6px; }

  .return-address {
    position: absolute; left: 17px; top: 296px;
    width: 241px; height: 166px;
    background: #fff; border-radius: 6px;
    text-align: center;
    font-family: "Quicksand", sans-serif;
    color: var(--ink-grey);
  }
  .return-address__mark {
    width: 30px; height: 30px; background: #b3b4d0;
    margin: 22px auto 10px;
  }
  .return-address__name { font-size: 22px; letter-spacing: 1px; text-transform: uppercase; margin-bottom: 8px; }
  .return-address__line { font-size: 15px; line-height: 1.3; }

  .stamp-box {
    position: absolute; left: 446px; top: 34px;
    width: 142px; height: 128px;
    border: 1px solid #cfcfcf; border-radius: 3px;
  }
  .address-lines { position: absolute; left: 324px; top: 237px; width: 264px; }
  .address-lines span {
    display: block; height: 37px;
    border-bottom: 1px dotted var(--rule-grey);
  }
</style>
</head>
<body>
  <section class="postcard postcard--front">
    <div class="front-photo" role="img" aria-label="Close-up photo of a wrapped red gift with a silver ribbon bow against purple and pink bokeh lights"></div>
    <svg class="ribbon" viewBox="0 0 184 212" aria-hidden="true">
      <polygon points="0,0 184,0 184,212 92,158 0,212" fill="#fff"/>
      <polyline points="10,0 10,194 92,146 174,194 174,0" fill="none" stroke="var(--ribbon-dots)" stroke-width="1.5" stroke-dasharray="1 4"/>
    </svg>
    <div class="ribbon__mark"></div>
    <div class="ribbon__name">Brantley Law</div>
    <h1 class="greeting"><span class="line-1">Happy</span><span class="line-2">Birthday</span></h1>
    <div class="sender">
      <p class="sender__lead">from the team at</p>
      <p class="sender__firm">Brantley Law Firm</p>
    </div>
  </section>

  <section class="postcard postcard--back">
    <div class="back-photo" role="img" aria-label="Soft-focus photo of the gift and ribbon in deep maroon tones"></div>
    <div class="contact">
      <p class="contact__tagline">Its About Taking</p>
      <p class="contact__value-word">Responsibility</p>
      <p class="contact__label">Call Us:</p>
      <p class="contact__number">(417) 555-0142</p>
      <p class="contact__label contact__label--small">Toll Free:</p>
      <p class="contact__number contact__number--toll">1-800-555-0199</p>
    </div>
    <div class="return-address">
      <div class="return-address__mark"></div>
      <p class="return-address__name">Brantley Law</p>
      <p class="return-address__line">7150 W Copperfield Ave</p>
      <p class="return-address__line">Springfield, MO 65817</p>
    </div>
    <div class="stamp-box"></div>
    <div class="address-lines"><span></span><span></span><span></span><span></span><span></span></div>
  </section>
</body>
</html>
```